Corvanta LLC, providing clean, low emission fuel for the transport and maritime industry

Corvanta LLC is a Texas based company dedicated to the development of Small Scale LNG projects with the objective of supplying clean, low emission fuel to the transport and maritime industry.

The design should be simple and sophisticated. We want a design that includes our company logo and uses our company logo colors. The site should include 7 pages (Home, About, What is LNG, Projects, Announcements and Contact Us). The site should ultimately be editable and capable of being imported into WIX. The design should communicate an environmentally conscious company who provide "Simple, Practical, and Cost Effective Solutions". Our competitions website looks like this www.brenmarfuel.com.

Target Market(s)

LNG, maritime

Industry/Entity Type

Oil And Gas

Coding

Coded - Design and coding required

Number of Pages Required

5+ page

Requirements
Must have
• Equal or better than our competitors website www.brenmarfuel.com
Company Logo.
The tagline "Simple, Practical, and Cost Effective Solutions"
Nice to have
• The page content will be very similar to our competitors website www.brenmarfuel.com
Should not have
• No red or black colours.

```html
<!DOCTYPE html>
<html lang="en">
<head>
<meta charset="utf-8">
<title>Corvanta LLC</title>
<link href="https://fonts.googleapis.com/css2?family=Montserrat:wght@400;500;600;700&display=swap" rel="stylesheet">
<style>
:root{
  --navy:#1b2f5c;
  --blue:#0e5aa6;
  --blue-dark:#0b3f86;
  --green:#3b9a3f;
  --text:#333;
  --muted:#777;
  --light:#f4f6fa;
  --line:#c9ccd3;
  --white:#fff;
}
*{box-sizing:border-box;margin:0;padding:0}
html,body{width:1200px;height:3578px;overflow:hidden}
body{position:relative;font-family:'Montserrat',sans-serif;color:var(--text);background:var(--white)}
.abs{position:absolute}
a{color:inherit;text-decoration:none}
ul{list-style:none}

/* header */
.site-header{position:absolute;left:0;top:0;width:1200px;height:87px;background:var(--white)}
.brand{position:absolute;left:160px;top:26px;display:flex;align-items:center;gap:8px;font-weight:700;font-size:16px;color:var(--navy)}
.brand .dot{width:24px;height:24px;border-radius:50%;background:var(--green)}
.top-contact{position:absolute;right:163px;top:21px;display:flex;gap:26px;font-size:11.5px;color:var(--navy)}
.top-contact span{display:flex;align-items:center;gap:7px}
.main-nav{position:absolute;right:163px;top:56px;display:flex;gap:28px;font-size:10px;font-weight:600;color:var(--navy)}
.main-nav .active{color:var(--green)}

/* hero */
.hero{position:absolute;left:0;top:87px;width:1200px;height:463px;background:linear-gradient(180deg,#4c6f9e 0%,#3a6298 35%,#2c5590 70%,#1f4a85 100%)}
.hero h1{position:absolute;left:160px;top:86px;font-size:36px;font-weight:600;color:var(--white)}
.hero p{position:absolute;left:162px;top:142px;width:680px;font-size:12.5px;line-height:22px;color:var(--white)}
.hero .btn-light{position:absolute;left:162px;top:204px;width:197px;height:42px;background:var(--white);color:var(--blue);border-radius:3px;font-size:13.5px;display:flex;align-items:center;justify-content:center}
.hero-emblem{position:absolute;left:579px;top:529px;width:42px;height:42px;border-radius:50%;background:var(--white);box-shadow:0 2px 6px rgba(0,0,0,.2);display:flex;align-items:center;justify-content:center}
.hero-emblem span{width:18px;height:18px;border-radius:50%;background:var(--green)}

/* intro */
.section-title{position:absolute;left:0;width:1200px;text-align:center;font-size:28px;font-weight:600;color:var(--navy)}
.section-sub{position:absolute;left:0;width:1200px;text-align:center;font-size:13px;color:#555}
.intro-photo{position:absolute;left:161px;top:733px;width:415px;height:408px;background:linear-gradient(135deg,#9aa8b8,#5a6f8d 55%,#2d3f6b)}
.feature h3{position:absolute;left:611px;font-size:17px;font-weight:600;color:#111}
.feature p{position:absolute;left:612px;width:415px;font-size:12.5px;line-height:23.3px;color:var(--muted)}
.btn-blue{position:absolute;background:linear-gradient(180deg,#1673bf,var(--blue-dark));color:var(--white);border-radius:3px;display:flex;align-items:center;justify-content:center;box-shadow:0 3px 6px rgba(0,0,0,.2)}

/* why */
.why{position:absolute;left:0;top:1227px;width:1200px;height:561px;background:var(--light)}
.why-card{position:absolute;width:278px;height:137px;background:var(--white);box-shadow:0 2px 10px rgba(0,0,0,.08);padding:26px 24px 0 26px}
.why-card h4{font-size:11.5px;font-weight:700;color:var(--navy);margin-bottom:9px}
.why-card p{font-size:11.5px;line-height:17px;color:var(--navy)}
.why-card.active{border-bottom:3px solid var(--blue-dark)}
.why-photo{position:absolute;left:452px;top:1406px;width:292px;height:292px;border-radius:50%;border:6px solid var(--blue-dark);background:linear-gradient(180deg,#c9d6e4,#8aa5c2 55%,#3f5f88)}
.why-icon{position:absolute;width:66px;height:66px;border-radius:50%;background:var(--white);border:3px solid var(--green);box-shadow:0 2px 6px rgba(0,0,0,.2);display:flex;align-items:center;justify-content:center}

/* contact form */
.contact-mark{position:absolute;left:433px;top:1835px;width:334px;height:445px;background:radial-gradient(ellipse at center,rgba(59,154,63,.06),rgba(14,90,166,.03) 70%,transparent 72%)}
.field{position:absolute;height:37px;border:1px solid var(--line);border-radius:4px;background:rgba(255,255,255,.6);font-size:11px;color:#888;padding:11px 17px}

/* testimonials */
.reviews{position:absolute;left:0;top:2318px;width:1200px;height:760px;background:linear-gradient(180deg,#1c4f99,#134a96 50%,#0d4492)}
.client-row{position:absolute;left:161px;top:2470px;width:877px;display:flex;justify-content:space-between;font-size:24px;font-weight:600;color:rgba(255,255,255,.55)}
.client-line{position:absolute;left:161px;top:2525px;width:877px;height:1px;background:rgba(255,255,255,.35)}
.quote-card{position:absolute;background:var(--white);box-shadow:0 3px 10px rgba(0,0,0,.2);font-size:10.5px;line-height:17px;color:#333;text-align:center}
.quote-badge{position:absolute;width:46px;height:46px;border-radius:50%;background:var(--white);box-shadow:0 2px 6px rgba(0,0,0,.25);color:var(--blue);font-size:40px;font-weight:700;line-height:62px;text-align:center}
.reviewer{position:absolute;text-align:center;color:var(--white)}
.reviewer b{display:block;font-size:12px;font-weight:600}
.reviewer span{font-size:10px}
.dots{position:absolute;left:580px;top:2869px;display:flex;gap:8px}
.dots span{width:8px;height:8px;border-radius:50%;background:#4aa3ff}
.dots span.on{background:var(--white)}

/* cta */
.cta{position:absolute;left:161px;top:2962px;width:877px;height:251px;background:var(--white);box-shadow:0 3px 12px rgba(0,0,0,.1)}
.cta h2{margin-top:46px;text-align:center;font-size:28px;font-weight:600;color:var(--navy)}
.cta p{margin-top:8px;text-align:center;font-size:12.5px;line-height:22px;color:#333}
.btn-outline{position:absolute;border:1.5px solid var(--blue-dark);border-radius:3px;color:var(--navy);display:flex;align-items:center;justify-content:center}

/* footer */
.footer-brand{position:absolute;left:161px;top:3300px;width:183px;height:170px;display:flex;flex-direction:column;align-items:center;justify-content:center;gap:14px}
.footer-brand .dot{width:70px;height:70px;border-radius:50%;background:var(--green)}
.footer-brand b{font-size:22px;font-weight:700;color:var(--navy)}
.foot-col{position:absolute;top:3300px}
.foot-col h5{font-size:12.5px;font-weight:600;color:#222;margin-bottom:17px}
.foot-col li{font-size:11.5px;color:var(--blue);height:27px;display:flex;align-items:center;gap:9px}
.foot-col li::before{content:"";width:4px;height:4px;border-radius:50%;background:var(--blue)}
.quick li{font-size:12px;color:#555;height:37px;display:flex;align-items:center;gap:12px}
.quick li.big{font-size:16px;color:#666}
.follow{position:absolute;left:850px;top:3453px;display:flex;align-items:center;gap:6px;font-size:13px;color:#666}
.follow span.c{width:27px;height:27px;border-radius:50%;border:1px solid #666}
.legal-line{position:absolute;left:0;top:3528px;width:1200px;height:1px;background:#eee}
.legal{position:absolute;top:3552px;font-size:11px;color:#888}
.legal b{color:var(--green);font-weight:600}
.legal-links{right:162px;color:var(--blue)}
.legal-links i{font-style:normal;color:#888;margin:0 8px}
</style>
</head>
<body>

<header class="site-header">
  <div class="brand"><span class="dot"></span>Corvanta LLC</div>
  <div class="top-contact">
    <span><svg width="12" height="12" viewBox="0 0 24 24"><path fill="#1b2f5c" d="M6.6 10.8a15 15 0 0 0 6.6 6.6l2.2-2.2c.3-.3.7-.4 1-.2 1.1.4 2.3.6 3.6.6.6 0 1 .4 1 1V20c0 .6-.4 1-1 1A17 17 0 0 1 3 4c0-.6.4-1 1-1h3.5c.6 0 1 .4 1 1 0 1.3.2 2.5.6 3.6.1.3 0 .7-.2 1z"/></svg>+1-713-555-0142</span>
    <span><svg width="13" height="10" viewBox="0 0 24 18"><path fill="#1b2f5c" d="M0 0h24v18H0z"/><path fill="#fff" d="M1 1l11 8 11-8v2L12 11 1 3z"/></svg>info@corvantallc.com</span>
  </div>
  <nav class="main-nav">
    <a class="active">HOME</a><a>ABOUT</a><a>WHAT IS LNG</a><a>PROJECTS</a><a>ANNOUNCEMENTS</a><a>CONTACT US</a>
  </nav>
</header>

<section class="hero" role="img" aria-label="LNG carrier ship at sea with mountains behind">
  <h1>Simple, Practical &amp; Cost Effective Solutions</h1>
  <p>Corvanta LLC is a Texas based company dedicated to the development of Small Scale LNG projects with the objective of supplying clean, low emission fuel to the transport and maritime industry.</p>
  <a class="btn-light">Contact with Us</a>
</section>
<div class="hero-emblem"><span></span></div>

<h2 class="section-title" style="top:630px">Creating New Markets for Clean Energy</h2>
<p class="section-sub" style="top:685px">Lorem ipsum dolor sit amet, consectetur adipiscing elit sed do eiusmod tempor</p>
<div class="intro-photo" role="img" aria-label="Two engineers in hard hats at a gas processing plant"></div>
<div class="feature">
  <h3 style="top:736px">SAFE AND RELIABLE</h3>
  <p style="top:767px">Safe and reliable energy is vital to the United States &amp; the global market place. It is a force for good, providing light, heat and mobility to people around the world, and the midstream LNG sector plays a critical role in moving natural gas (energy) from its various sources of production to consumers.</p>
  <h3 style="top:901px">KEELPOINT LNG BUILDING</h3>
  <p style="top:932px">Keelpoint LNG is focused on building or acquiring midstream LNG assets in North America, and internationally across the value chain from delivered molecules at the pipeline, to the burner tip in power generation.Keelpoint's goal is to build and operate highly competitive new assets that serve the continually growing and changing needs of the North American and global G/natural.</p>
</div>
<a class="btn-blue" style="left:611px;top:1088px;width:160px;height:42px;font-size:13.5px">Read More</a>

<section class="why">
  <h2 class="section-title" style="top:80px">Why Our Clients Love Us</h2>
  <p class="section-sub" style="top:127px">Lorem ipsum dolor sit amet, consectetur adipiscing elit sed do eiusmod tempor</p>
</section>
<div class="why-card active" style="left:161px;top:1406px"><h4>WELL MANAGEMENT</h4><p>Duis aute irure dolor in reprehenderit in vptate velit esse cillum dolore eu fugiat nulla pariatur. Duis aute irure dolor in reprehend</p></div>
<div class="why-card" style="left:161px;top:1564px"><h4>COMPLETIONS</h4><p>Duis aute irure dolor in reprehenderit in vptate velit esse cillum dolore eu fugiat nulla pariatur. Duis aute irure dolor in reprehend</p></div>
<div class="why-card" style="left:760px;top:1406px"><h4>GEOSCIENCE RESEARCH</h4><p>Duis aute irure dolor in reprehenderit in vptate velit esse cillum dolore eu fugiat nulla pariatur. Duis aute irure dolor in reprehend</p></div>
<div class="why-card" style="left:760px;top:1564px"><h4>SERVICES QUALITY</h4><p>Duis aute irure dolor in reprehenderit in vptate velit esse cillum dolore eu fugiat nulla pariatur. Duis aute irure dolor in reprehend</p></div>
<div class="why-photo" role="img" aria-label="Offshore drilling platform with supply vessel"></div>
<div class="why-icon" style="left:454px;top:1419px"><svg width="30" height="30" viewBox="0 0 24 24"><circle cx="12" cy="12" r="7" fill="none" stroke="#1b2f5c" stroke-width="2" stroke-dasharray="3 2"/><circle cx="12" cy="12" r="3" fill="none" stroke="#1b2f5c" stroke-width="1.5"/></svg></div>
<div class="why-icon" style="left:676px;top:1419px"><svg width="28" height="28" viewBox="0 0 24 24"><rect x="4" y="3" width="13" height="17" fill="none" stroke="#1b2f5c" stroke-width="1.5"/><path d="M7 8h7M7 11h7M7 14h4" stroke="#1b2f5c" stroke-width="1.5"/><circle cx="17" cy="16" r="3" fill="none" stroke="#1b2f5c" stroke-width="1.5"/></svg></div>
<div class="why-icon" style="left:454px;top:1620px"><svg width="28" height="28" viewBox="0 0 24 24"><rect x="3" y="5" width="18" height="16" rx="2" fill="none" stroke="#1b2f5c" stroke-width="1.5"/><path d="M3 9h18" stroke="#1b2f5c" stroke-width="1.5"/><path d="M8 15l3 3 5-6" fill="none" stroke="#1b2f5c" stroke-width="1.5"/></svg></div>
<div class="why-icon" style="left:676px;top:1620px"><svg width="28" height="28" viewBox="0 0 24 24"><circle cx="12" cy="13" r="8" fill="none" stroke="#1b2f5c" stroke-width="1.5"/><path d="M12 13V8M10 3h4" stroke="#1b2f5c" stroke-width="1.5"/></svg></div>

<section class="contact">
  <div class="contact-mark"></div>
  <h2 class="section-title" style="top:1866px">Contact With Us</h2>
  <p class="section-sub" style="top:1912px">Lorem ipsum dolor sit amet, consectetur adipiscing elit sed do eiusmod tempor</p>
  <div class="field" style="left:274px;top:1951px;width:314px">Name</div>
  <div class="field" style="left:611px;top:1951px;width:315px">Email</div>
  <div class="field" style="left:274px;top:2005px;width:314px">Phone</div>
  <div class="field" style="left:611px;top:2005px;width:315px">Subject</div>
  <div class="field" style="left:274px;top:2060px;width:652px;height:104px">Message</div>
  <a class="btn-blue" style="left:386px;top:2185px;width:428px;height:48px;font-size:13px;font-weight:700">SUBMIT NOW</a>
</section>

<section class="reviews">
  <h2 class="section-title" style="top:82px;color:#fff">What our client say about Us</h2>
</section>
<div class="client-row"><span>Northwave</span><span>Brightlane</span><span>Tidemark</span><span>Verasol</span><span>Harbor Daily</span></div>
<div class="client-line"></div>

<div class="quote-card" style="left:161px;top:2593px;width:254px;height:160px;padding:42px 14px 0">"Lorem ipsum dolor sit amet, consectetur adipiscing elit, sed do eiusmod tempor incididunt ut labore et dolore magna aliqua. Ut enim ad minim veniam, quis nostrud exercitation ullamco laboris nisi ut aliquip ex ea commodo consequat".</div>
<div class="quote-badge" style="left:265px;top:2566px">”</div>
<div class="reviewer" style="left:161px;top:2775px;width:254px"><b>Lucas Moreau</b><span>Happy Client</span></div>

<div class="quote-card" style="left:451px;top:2593px;width:298px;height:181px;padding:42px 26px 0">"Lorem ipsum dolor sit amet, consectetur adipiscing elit, sed do eiusmod tempor incididunt ut labore et dolore magna aliqua. Ut enim ad minim veniam, quis nostrud exercitation ullamco laboris nisi ut aliquip ex ea commodo consequat. Duis aute irure dolor in reprehenderit."</div>
<div class="quote-badge" style="left:573px;top:2560px;width:54px;height:54px;font-size:46px;line-height:72px">”</div>
<div class="reviewer" style="left:451px;top:2802px;width:298px"><b>Henri Delacroix</b><span>Happy Client</span></div>

<div class="quote-card" style="left:785px;top:2593px;width:254px;height:131px;padding:36px 16px 0">"Lorem ipsum dolor sit amet, consectetur adipiscing elit, sed do eiusmod tempor incididunt ut labore et dolore magna aliqua. Ut enim ad minim veniam, quis nostrud exercitation ullamco laboris nisi"</div>
<div class="quote-badge" style="left:889px;top:2568px">”</div>
<div class="reviewer" style="left:785px;top:2758px;width:254px"><b>Paul Lindqvist</b><span>Happy Client</span></div>

<div class="dots"><span></span><span class="on"></span><span></span></div>

<section class="cta">
  <h2>Our experts are ready to help you</h2>
  <p>Lorem ipsum dolor sit amet, consectetur adipiscing elit, sed do eiusmod tempor<br>incididunt ut labore et dolore magna aliqua.</p>
  <a class="btn-blue" style="left:202px;top:149px;width:225px;height:54px;font-size:19px">Get A Quote</a>
  <a class="btn-outline" style="left:450px;top:149px;width:225px;height:54px;font-size:19px">Contact Us</a>
</section>

<footer>
  <div class="footer-brand"><span class="dot"></span><b>Corvanta LLC</b></div>
  <div class="foot-col" style="left:438px"><h5>Services</h5>
    <ul><li>Home</li><li>About</li><li>What is LNG</li><li>Projects</li><li>Announcements</li><li>Contact Us</li></ul></div>
  <div class="foot-col" style="left:627px"><h5>Other Links</h5>
    <ul><li>Lorem ipsum</li><li>Dolor sit amet</li><li>Consectetur elit</li><li>Sed do eiusmod</li><li>Tempor incididunt</li><li>Labore et dolore</li></ul></div>
  <div class="foot-col quick" style="left:850px"><h5 style="margin-bottom:6px">Quick Contact</h5>
    <ul>
      <li><svg width="13" height="10" viewBox="0 0 24 18"><path fill="#1b2f5c" d="M0 0h24v18H0z"/><path fill="#fff" d="M1 1l11 8 11-8v2L12 11 1 3z"/></svg><span style="color:#1b2f5c;font-weight:600">info@corvantallc.com</span></li>
      <li class="big"><svg width="12" height="12" viewBox="0 0 24 24"><path fill="#1b2f5c" d="M6.6 10.8a15 15 0 0 0 6.6 6.6l2.2-2.2c.3-.3.7-.4 1-.2 1.1.4 2.3.6 3.6.6.6 0 1 .4 1 1V20c0 .6-.4 1-1 1A17 17 0 0 1 3 4c0-.6.4-1 1-1h3.5c.6 0 1 .4 1 1 0 1.3.2 2.5.6 3.6.1.3 0 .7-.2 1z"/></svg>+1-713-555-0142</li>
      <li class="big"><svg width="12" height="12" viewBox="0 0 24 24"><path fill="#1b2f5c" d="M6 3h12v5H6zM3 9h18v8h-3v4H6v-4H3z"/></svg>+1-713-555-0187</li>
    </ul></div>
  <div class="follow">Follow Us :&nbsp;<span class="c"></span><span class="c"></span><span class="c"></span></div>
  <div class="legal-line"></div>
  <p class="legal" style="left:162px">© 2020 <b>CORVANTA LLC</b> All Rights Reserved.</p>
  <p class="legal legal-links">About Us<i>/</i>Sitemap<i>/</i>Privacy Policy<i>/</i>Contact Us</p>
</footer>

</body>
</html>
```